Fence & Deck Construction Flyer

My company is called Brisholt Fence & Deck and I am seeking a flyer for direct marketing our construction services to residential customers in Calgary. Our focus is home owners aged 35+ that are looking to replace an old fence or deck, although we also do new construction. We use pressure treated wood mainly, but we also use cedar and composite products. You can view our website at www.brisholtfence.example for some additional insight and pictures of our previous projects. Company colors are black and deep yellow (see website).
The size of the flyer will need to be 6 inches by 11 inches, both sides in full colour.

```html
<!DOCTYPE html>
<html lang="en">
<head>
<meta charset="utf-8">
<title>Brisholt Fence &amp; Deck – Flyer</title>
<link rel="stylesheet" href="https://fonts.googleapis.com/css2?family=Bebas+Neue&family=Oswald:wght@500;700&display=swap">
<style>
  :root {
    --sky-top: #2f9fab;
    --sky-light: #6fd5db;
    --teal: #2b8e98;
    --teal-deep: #1f6570;
    --panel-teal: #14838a;
    --yellow: #f2c500;
    --yellow-deep: #d8a900;
    --card-frame: #333a3c;
    --label-brown: #5a360c;
    --white: #ffffff;
    --free-blue: #7fd0ee;
    --wood: #9a5a26;
    --grass: #5fb53a;
  }
  * { margin: 0; padding: 0; box-sizing: border-box; }
  html, body { width: 1200px; height: 2198px; overflow: hidden; }
  body { font-family: "Bebas Neue", "Oswald", sans-serif; color: var(--white); }

  .flyer {
    position: relative;
    width: 1200px;
    height: 2198px;
    overflow: hidden;
    background: linear-gradient(to bottom,
      var(--sky-top) 0px,
      var(--sky-light) 520px,
      var(--teal) 820px,
      var(--teal) 1500px,
      var(--teal-deep) 2198px);
  }
  .abs { position: absolute; }

  .brand-name {
    top: 8px; left: 0; width: 100%;
    text-align: center;
    font-size: 84px; letter-spacing: 2px;
    color: var(--yellow);
    line-height: 1;
  }
  .headline {
    top: 100px; left: 0; width: 100%;
    text-align: center;
    font-size: 132px; letter-spacing: 3px;
    line-height: 1;
  }
  .lead-in {
    top: 250px; left: 38px;
    font-size: 54px; letter-spacing: 1px; line-height: 1;
  }
  .pointer { top: 256px; left: 80px; }
  .tagline {
    top: 344px; left: 330px;
    font-family: "Oswald", sans-serif; font-weight: 500;
    font-size: 28px; letter-spacing: 0.5px;
  }

  .fence-art {
    top: 559px; left: 0; width: 1200px; height: 260px;
    background: linear-gradient(to bottom, var(--wood) 0%, #8a4f20 70%, var(--grass) 78%, #3f8f27 100%);
  }

  .products { top: 846px; left: 33px; width: 1150px; display: flex; gap: 14px; }
  .product { width: 374px; }
  .product-photo {
    height: 356px;
    border: 14px solid var(--card-frame);
    background: linear-gradient(to bottom, #9fb8c8 0%, #b7aa95 45%, #8f8270 100%);
  }
  .product-info {
    height: 264px; margin-top: 2px;
    border: 3px solid var(--yellow-deep);
    background: linear-gradient(to bottom, var(--yellow) 0%, var(--yellow-deep) 100%);
    padding: 22px 16px 0;
  }
  .product-name {
    font-family: "Oswald", sans-serif; font-weight: 700;
    font-size: 27px; color: var(--label-brown);
    text-decoration: underline;
  }
  .product-from {
    margin-top: 44px;
    font-family: "Oswald", sans-serif; font-weight: 700;
    font-size: 27px; color: var(--label-brown);
  }
  .product-price { margin-top: 4px; font-size: 60px; line-height: 1; letter-spacing: 1px; }

  .quote-line {
    top: 1496px; left: 0; width: 100%; text-align: center;
    font-size: 52px; letter-spacing: 1px; line-height: 1;
  }
  .quote-line .free { color: var(--free-blue); }
  .web {
    top: 1572px; left: 0; width: 100%; text-align: center;
    font-size: 72px; color: var(--yellow); letter-spacing: 2px; line-height: 1;
  }
  .phone {
    top: 1655px; left: 490px;
    font-size: 52px; letter-spacing: 2px; line-height: 1;
  }

  .quote-badge {
    top: 1633px; left: 6px; width: 410px; height: 410px;
    border-radius: 50%;
    background: var(--yellow-deep);
    display: flex; flex-direction: column; align-items: center; justify-content: center;
    text-align: center;
  }
  .quote-badge .big { font-size: 54px; line-height: 1.15; letter-spacing: 1px; }
  .quote-badge .small { font-family: "Oswald", sans-serif; font-weight: 500; font-size: 22px; margin-top: 4px; }

  .card-slot {
    top: 1722px; left: 482px; width: 683px; height: 300px;
    background: var(--panel-teal);
    display: flex; align-items: center; justify-content: center;
    font-size: 44px; letter-spacing: 1px;
  }

  .rule { top: 2068px; left: 0; width: 100%; height: 4px; background: var(--yellow); }
  .motto {
    top: 2090px; left: 0; width: 100%; text-align: center;
    font-size: 112px; letter-spacing: 3px; line-height: 1;
  }
</style>
</head>
<body>
<main class="flyer">
  <h2 class="abs brand-name">Brisholt Fence &amp; Deck</h2>
  <h1 class="abs headline">Is your fence broken?</h1>
  <p class="abs lead-in">This is where we come in</p>
  <svg class="abs pointer" width="30" height="280" viewBox="0 0 30 280" aria-hidden="true">
    <line x1="15" y1="0" x2="15" y2="272" stroke="#fff" stroke-width="4"/>
    <polyline points="3,254 15,274 27,254" fill="none" stroke="#fff" stroke-width="4"/>
  </svg>
  <p class="abs tagline">FENCING DONE THE PROFFESIONAL WAY</p>

  <div class="abs fence-art" role="img" aria-label="Wooden picket fence with a broken section, standing in green grass"></div>

  <section class="abs products">
    <article class="product">
      <div class="product-photo" role="img" aria-label="Finished pressure treated spruce deck in a backyard"></div>
      <div class="product-info">
        <div class="product-name">PRESSURE TREATED SPRUCE</div>
        <div class="product-from">STARTING FROM</div>
        <div class="product-price">$12 SQAURE. FT.</div>
      </div>
    </article>
    <article class="product">
      <div class="product-photo" role="img" aria-label="Western red cedar deck with privacy screen beside a house"></div>
      <div class="product-info">
        <div class="product-name">WESTERN RED CEDAR</div>
        <div class="product-from">STARTING FROM</div>
        <div class="product-price">$15 SQUARE. FT.</div>
      </div>
    </article>
    <article class="product">
      <div class="product-photo" role="img" aria-label="Composite deck with steps and privacy screen"></div>
      <div class="product-info">
        <div class="product-name">COMPOSITE DECKING</div>
        <div class="product-from">STARTING FROM</div>
        <div class="product-price">$22 SQUARE. FT.</div>
      </div>
    </article>
  </section>

  <p class="abs quote-line">Get <span class="free">free</span> qoutation if you call or request one online</p>
  <p class="abs web">www.brisholtfence.example</p>
  <p class="abs phone">403-555-0147</p>

  <div class="abs quote-badge">
    <div class="big">FREE QOUTATION<br>WHEN</div>
    <div class="small">YOU CALL US OR VISIT US ONLINE.</div>
  </div>

  <div class="abs card-slot">STICK BUSINESS CARD HERE</div>

  <div class="abs rule"></div>
  <p class="abs motto">Trusted, secure, reliable</p>
</main>
</body>
</html>
```